Dunmore Plumbing LLC business card

Would like a modern looking business card with my new logo

Contact Information for Business Card

Calvin Dunmore 2418 Elm Hollow Rd Southbury, CT 06999, Dunmoreplumbingllc@exampletrade.com, 203-555-0174

```html
<!DOCTYPE html>
<html lang="en">
<head>
<meta charset="utf-8">
<title>Dunmore Plumbing LLC — Business Card</title>
<link rel="stylesheet" href="https://fonts.googleapis.com/css2?family=Open+Sans:wght@400;800&display=swap">
<style>
  :root {
    --page: #ecebe8;
    --card: #ffffff;
    --ink: #161616;
    --muted: #444444;
    --blue: #27aae1;
    --shadow: rgba(0,0,0,0.14);
  }
  * { margin: 0; padding: 0; box-sizing: border-box; }
  html, body { width: 1200px; height: 1200px; overflow: hidden; }
  body {
    background: var(--page);
    font-family: "Open Sans", sans-serif;
    display: flex;
    flex-direction: column;
    align-items: center;
    justify-content: center;
    gap: 70px;
  }
  .card {
    position: relative;
    width: 700px;
    height: 400px;
    background: var(--card);
    box-shadow: 0 8px 24px var(--shadow);
    overflow: hidden;
  }
  /* Front */
  .card-front .band {
    position: absolute;
    left: 0; right: 0;
    top: 272px; height: 78px;
    background: var(--blue);
  }
  .card-front .faucet-art {
    position: absolute;
    left: 0; top: 70px;
    width: 260px; height: 200px;
    background: linear-gradient(180deg, #1c1c1c 0%, #2a2a2a 70%, var(--blue) 100%);
    border-radius: 0 18px 60px 0;
  }
  .wordmark {
    font-weight: 800;
    color: var(--ink);
    text-transform: uppercase;
    letter-spacing: 0.02em;
    line-height: 1;
    display: flex;
    align-items: center;
    gap: 12px;
  }
  .wordmark .mark-square {
    width: 18px; height: 18px;
    background: var(--blue);
    flex: none;
  }
  .card-front .wordmark {
    position: absolute;
    left: 320px; top: 58px;
    font-size: 30px;
  }
  .card-front .details {
    position: absolute;
    left: 320px; top: 128px;
  }
  .name {
    font-size: 24px;
    font-weight: 400;
    color: var(--blue);
    text-transform: uppercase;
    line-height: 1.1;
  }
  .role {
    font-size: 14px;
    color: var(--muted);
    margin-bottom: 14px;
  }
  .contact {
    list-style: none;
    font-size: 14px;
    color: var(--muted);
  }
  .contact li {
    display: flex;
    align-items: center;
    gap: 8px;
    height: 22px;
  }
  .contact svg { width: 13px; height: 13px; flex: none; }
  /* Back */
  .card-back {
    display: flex;
    align-items: center;
    justify-content: center;
  }
  .card-back .wordmark { font-size: 40px; }
  .card-back .wordmark .mark-square { width: 24px; height: 24px; }
</style>
</head>
<body>
  <section class="card card-front" aria-label="Business card front">
    <div class="band"></div>
    <div class="faucet-art" role="img" aria-label="Illustration of a black water faucet with a blue drop"></div>
    <div class="wordmark"><span class="mark-square"></span>Dunmore Plumbing LLC</div>
    <div class="details">
      <p class="name">Calvin Dunmore</p>
      <p class="role">Founder</p>
      <ul class="contact">
        <li>
          <svg viewBox="0 0 16 16" aria-hidden="true"><path fill="#27aae1" d="M3.6 1.5l2.3 2.6-1.3 1.8c.9 2 2.5 3.6 4.5 4.5l1.8-1.3 2.6 2.3-1.4 2.1C6.8 13.4 2.6 9.2 1.5 3z"/></svg>
          203-555-0174
        </li>
        <li>
          <svg viewBox="0 0 16 16" aria-hidden="true"><circle cx="8" cy="8" r="6.5" fill="none" stroke="#27aae1" stroke-width="1.6"/><path d="M1.5 8h13M8 1.5c3 3.5 3 9.5 0 13M8 1.5c-3 3.5-3 9.5 0 13" fill="none" stroke="#27aae1" stroke-width="1.2"/></svg>
          www.dunmoreplumbing.example
        </li>
        <li>
          <svg viewBox="0 0 16 16" aria-hidden="true"><rect x="1" y="3" width="14" height="10" fill="#27aae1"/><path d="M1 3l7 6 7-6" fill="none" stroke="#fff" stroke-width="1.2"/></svg>
          Dunmoreplumbingllc@exampletrade.com
        </li>
      </ul>
    </div>
  </section>

  <section class="card card-back" aria-label="Business card back">
    <div class="wordmark"><span class="mark-square"></span>Dunmore Plumbing LLC</div>
  </section>
</body>
</html>
```